Some good designs here, but modifications required:
1) in the UK, we refer to cell phones as mobile phones, so the number should be written with an 'M' rather than a 'C' before it, or 'Mobile' rather than 'Cell'.
2) ensure that the compliment slip includes the business address and contact details, with the email address: info@brightarc-mail.com.
3) I prefer the 'with compliments' to go in the bottom right hand corner, thereby leaving space for a note on the compliment slip.
I have just had a new logo designed, but have not yet received it to upload. Please see Vela Grin Logo competition (now closed) where draft 79 was the winner.
Business cards
A4 letterhead sheets
Compliment slips (one third of an A4 sheet)

```html
<!DOCTYPE html>
<html lang="en">
<head>
<meta charset="utf-8">
<title>Velagrin Stationery Set</title>
<link href="https://fonts.googleapis.com/css2?family=Arimo:wght@400;700&display=swap" rel="stylesheet">
<style>
  :root {
    --brand: #a3185c;
    --brand-deep: #86104a;
    --brand-light: #b8306f;
    --ink: #3a3a3a;
    --muted: #777;
    --edge: #9a9a9a;
    --paper: #ffffff;
  }
  * { box-sizing: border-box; margin: 0; padding: 0; }
  html, body { width: 1200px; height: 1104px; overflow: hidden; background: var(--paper); }
  body { position: relative; font-family: "Arimo", Arial, sans-serif; color: var(--ink); }

  .brand { display: flex; align-items: center; gap: 8px; font-weight: 700; color: var(--brand); letter-spacing: -0.5px; position: absolute; line-height: 1; white-space: nowrap; }
  .brand-dot { border-radius: 50%; background: var(--brand); flex: none; }
  .brand--white { color: #fff; }
  .brand--white .brand-dot { background: #fff; }

  .sheet { position: absolute; background: var(--paper); border: 1px solid var(--edge); }

  .contact { position: absolute; display: flex; white-space: nowrap; }
  .contact .col + .col { border-left: 1px solid var(--muted); margin-left: 12px; padding-left: 10px; }
  .contact b { color: var(--brand); font-weight: 700; display: inline-block; }
  .contact .col:first-child b { margin-right: 3px; }

  /* Letterhead */
  .letterhead { left: 15px; top: 15px; width: 790px; height: 1059px; }
  .letterhead .brand { left: 40px; top: 44px; font-size: 46px; }
  .letterhead .brand-dot { width: 18px; height: 18px; }
  .letterhead .web { position: absolute; left: 40px; top: 1025px; font-size: 9px; color: var(--brand); font-weight: 700; display: flex; align-items: center; gap: 4px; }
  .letterhead .web::before { content: ""; width: 8px; height: 8px; border-radius: 50%; background: var(--brand); }
  .letterhead .contact { left: 405px; top: 962px; font-size: 11px; line-height: 15px; }
  .letterhead .contact .col + .col b { width: 50px; }

  /* Business card front */
  .card { position: absolute; border-radius: 10px; overflow: hidden; }
  .card-front { left: 825px; top: 15px; width: 360px; height: 201px; background: var(--paper); border: 1px solid var(--edge); }
  .card-front .brand { left: 14px; top: 24px; font-size: 28px; }
  .card-front .brand-dot { width: 11px; height: 11px; }
  .card-front .address { position: absolute; left: 206px; top: 20px; font-size: 8px; line-height: 11px; }
  .card-front .address b { color: var(--brand); }
  .card-front .person { position: absolute; right: 162px; top: 96px; text-align: right; white-space: nowrap; }
  .card-front .person .name { color: var(--brand); font-weight: 700; font-size: 12px; }
  .card-front .person .role { font-size: 8px; color: var(--muted); margin-top: 2px; }
  .card-front .contact { left: 206px; top: 96px; font-size: 8px; line-height: 11px; }
  .card-front .contact .col { border-left: 1px solid var(--muted); padding-left: 6px; }
  .card-front .contact b { width: 34px; }

  /* Business card back */
  .card-back { left: 825px; top: 240px; width: 360px; height: 195px; background: linear-gradient(180deg, var(--brand-light), var(--brand-deep)); color: #fff; }
  .card-back .brand { left: 18px; top: 70px; font-size: 28px; }
  .card-back .brand-dot { width: 11px; height: 11px; }
  .card-back .services { position: absolute; left: 178px; top: 18px; font-size: 9px; line-height: 15px; border-left: 1px solid rgba(255,255,255,.6); padding-left: 10px; }
  .card-back .services h3 { font-size: 11px; font-weight: 700; margin-bottom: 3px; }
  .card-back .services li { list-style: none; padding-left: 10px; position: relative; }
  .card-back .services li::before { content: ""; position: absolute; left: 0; top: 6px; width: 4px; height: 4px; background: #fff; }
  .card-back .web { position: absolute; left: 50px; top: 162px; font-size: 8px; font-weight: 700; }

  /* Compliment slip */
  .slip { left: 345px; top: 640px; width: 840px; height: 318px; }
  .slip .band { position: absolute; left: 0; top: 0; width: 100%; height: 92px; background: linear-gradient(90deg, var(--brand-deep), var(--brand-light) 50%, var(--brand-deep)); }
  .slip .brand { left: 40px; top: 122px; font-size: 32px; }
  .slip .brand-dot { width: 13px; height: 13px; }
  .slip .contact { left: 488px; top: 176px; font-size: 8px; line-height: 11px; }
  .slip .contact .col + .col b { width: 34px; }
  .slip .greeting { position: absolute; right: 30px; bottom: 22px; font-size: 14px; font-weight: 700; color: var(--brand); }
</style>
</head>
<body>

<section class="sheet letterhead" aria-label="Letterhead">
  <div class="brand"><span class="brand-dot"></span>Velagrin</div>
  <div class="contact">
    <div class="col">
      <b>Address:</b>Vela Grin Ltd<br>Westbury Dental Centre<br>48 Harlow Crescent<br>London, NW3 8QT
    </div>
    <div class="col">
      <b>Phone:</b>+44 (0) 20 7946 0381<br>
      <b>Mobile:</b>+44 (0) 7700 90 0472<br>
      <b>Fax:</b>+44 (0) 20 7946 0392<br>
      <b>Email:</b>info@brightarc-mail.com
    </div>
  </div>
  <div class="web">velagrin.com</div>
</section>

<section class="card card-front" aria-label="Business card front">
  <div class="brand"><span class="brand-dot"></span>Velagrin</div>
  <div class="address"><b>Address:</b> Vela Grin Ltd<br>Westbury Dental Centre<br>48 Harlow Crescent<br>London, NW3 8QT</div>
  <div class="person">
    <div class="name">Dr Corin Ashby</div>
    <div class="role">BDS MSc MOrth RCS</div>
    <div class="role">Orthodontic Director</div>
  </div>
  <div class="contact">
    <div class="col">
      <b>Phone</b>+44 (0) 20 7946 0381<br>
      <b>Mobile</b>+44 (0) 7700 90 0472<br>
      <b>Fax</b>+44 (0) 20 7946 0392<br>
      <b>Email</b>corin@brightarc-mail.com
    </div>
  </div>
</section>

<section class="card card-back" aria-label="Business card back">
  <div class="brand brand--white"><span class="brand-dot"></span>Velagrin</div>
  <div class="services">
    <h3>List of Services</h3>
    <ul>
      <li>Cosmetic Dentistry</li>
      <li>Orthodontics</li>
      <li>Clear Aligners</li>
      <li>Lingual Braces</li>
      <li>Oral Maxillofacial Surgery</li>
      <li>Periodontics</li>
      <li>Endodontics</li>
    </ul>
  </div>
  <div class="web">velagrin.com</div>
</section>

<section class="sheet slip" aria-label="Compliment slip">
  <div class="band"></div>
  <div class="brand"><span class="brand-dot"></span>Velagrin</div>
  <div class="contact">
    <div class="col">
      <b>Address:</b>Vela Grin Ltd<br>Westbury Dental Centre<br>48 Harlow Crescent<br>London, NW3 8QT
    </div>
    <div class="col">
      <b>Phone</b>+44 (0) 20 7946 0381<br>
      <b>Mobile</b>+44 (0) 7700 90 0472<br>
      <b>Fax</b>+44 (0) 20 7946 0392<br>
      <b>Email</b>info@brightarc-mail.com
    </div>
  </div>
  <p class="greeting">with compliments</p>
</section>

</body>
</html>
```